Pediatric Practice Flyer Design

I need marketing flyer created for distribution. It is for a pediatric clinic. Need some realistic eye catching design and content. I already have a logo that will go on top of the flyer. I will be using corbelwade for flyer print service. So need it copyable for printing. Again, need eye catching content as well. We are planning on opening the clinic in December.

```html
<!DOCTYPE html>
<html lang="en">
<head>
<meta charset="utf-8">
<title>Maple Grove Kids Pediatrics – Opening Flyer</title>
<link href="https://fonts.googleapis.com/css2?family=Poppins:wght@300;400;500;600;700;800&display=swap" rel="stylesheet">
<style>
  :root{
    --red:#e8262f;
    --blue:#1667b4;
    --teal:#1a9a8a;
    --orange:#f5931f;
    --pink:#e6177f;
    --purple:#7b2d8e;
    --ink:#2a2a2a;
    --body:#3a3a3a;
    --band:#e8e8ea;
    --page:#f1f1f2;
  }
  *{margin:0;padding:0;box-sizing:border-box}
  html,body{width:1200px;height:2602px;overflow:hidden;background:var(--page)}
  body{font-family:'Poppins',sans-serif;color:var(--body);position:relative}
  .flyer{position:absolute;left:50px;top:588px;width:1100px;height:1425px;background:#fff;overflow:hidden;box-shadow:0 6px 24px rgba(0,0,0,.12)}
  .abs{position:absolute}

  .hero-photo{left:0;top:0;width:1100px;height:500px}
  .accent-stripe{left:0;top:0;width:1100px;height:300px}
  .brand{left:56px;top:112px;display:flex;align-items:center;gap:16px}
  .brand-dot{width:54px;height:54px;border-radius:50%;background:var(--red)}
  .brand-name{font-weight:700;font-size:40px;line-height:1.05;color:var(--red);letter-spacing:-.5px}

  .welcome{left:56px;top:262px;font-weight:800;font-size:47px;line-height:50px;letter-spacing:-.5px}
  .welcome span{display:block}
  .welcome .l1{color:var(--ink)}
  .welcome .l2{color:var(--red)}
  .welcome .l3{color:var(--blue)}
  .welcome-sub{left:56px;top:428px;width:480px;font-size:17px;line-height:20px;color:var(--ink)}

  .teddy{left:555px;top:250px;width:310px;height:235px;border-radius:110px 110px 30px 30px;background:radial-gradient(circle at 35% 40%,#d9a266,#b77a3c 70%,#f1f1f1 71%)}

  .goal-band{left:0;top:504px;width:1100px;height:138px;background:var(--band)}
  .goal-pill{left:56px;top:528px;height:34px;padding:0 16px;background:var(--teal);color:#fff;font-weight:500;font-size:21px;line-height:34px;border-radius:3px}
  .goal-text{left:56px;top:572px;width:520px;font-size:18px;line-height:22px;color:var(--ink)}
  .goal-text .purple{color:var(--purple);font-weight:500}
  .goal-text .pink{color:var(--pink);font-weight:500}
  .note{top:520px;width:106px;height:108px}
  .note-star{left:586px;background:linear-gradient(135deg,#ffc64a,#f7a928)}
  .note-rocket{left:726px;background:linear-gradient(135deg,#ffffff,#ececec);border:1px solid #d8d8d8}
  .note-dream{left:862px;background:linear-gradient(135deg,#1d7fa3,#0f5f80)}

  .provider-photo{left:60px;top:677px;width:161px;height:171px;background:linear-gradient(180deg,#ecedef,#d9d4cf);border:3px solid #fff;box-shadow:0 0 0 1px #ddd}
  .provider-tag{left:56px;top:869px;width:168px;height:29px;background:var(--pink);color:#fff;font-weight:500;font-size:16px;line-height:29px;text-align:center;border-radius:2px}
  .bio{left:254px;top:666px;width:790px;font-size:15.5px;line-height:19px;color:var(--body)}
  .bio p{margin-bottom:19px}
  .bio .doc{color:var(--blue);font-weight:600}
  .bio-wide{left:56px;top:912px;width:990px;font-size:15.5px;line-height:19px;color:var(--body)}

  .kids-photo{left:56px;top:1100px;width:420px;height:270px;border-radius:120px 140px 110px 130px;border:6px solid var(--orange);background:linear-gradient(135deg,#f4f4f4,#dedede)}

  .coming{left:478px;top:1094px;width:566px;text-align:center;font-weight:600;font-size:34px;line-height:40px;color:var(--red)}
  .coming .teal{color:var(--teal)}
  .accepting{left:500px;top:1134px;width:540px;display:flex;align-items:center;gap:10px;font-weight:300;font-size:32px;line-height:40px;color:var(--ink)}
  .accepting::before,.accepting::after{content:"";flex:1;height:2px;background:var(--ink)}
  .red-band{left:478px;top:1180px;width:622px;height:51px;background:var(--red);clip-path:polygon(26px 0,100% 0,100% 100%,0 100%)}
  .red-band span{position:absolute;left:62px;top:0;font-weight:800;font-size:38px;line-height:51px;color:#fff;letter-spacing:.5px}
  .blue-band{left:463px;top:1238px;width:637px;height:32px;background:var(--blue);clip-path:polygon(16px 0,100% 0,100% 100%,0 100%)}
  .blue-band span{position:absolute;left:55px;top:0;font-weight:600;font-size:20px;line-height:32px;color:#fff}

  .phone-icon{left:478px;top:1294px;width:40px;height:40px;background:var(--pink);border-radius:6px}
  .phone-num{left:528px;top:1286px;font-weight:600;font-size:27px;line-height:32px;color:var(--ink);white-space:nowrap}
  .web{left:528px;top:1320px;font-size:11.5px;line-height:16px;color:var(--ink);display:flex;align-items:center;gap:5px;white-space:nowrap}
  .addr{left:736px;top:1294px;font-size:12.5px;line-height:16px;color:var(--ink);display:flex;align-items:center;gap:7px;white-space:nowrap}
  .contact2{left:736px;top:1320px;font-size:12.5px;line-height:16px;color:var(--ink);display:flex;align-items:center;gap:7px;white-space:nowrap}
  .sep{width:1px;height:16px;background:#888;margin:0 3px}
  .footer-band{left:0;top:1374px;width:1100px;height:51px;background:var(--band)}
  .register{left:476px;top:1358px;width:240px;height:34px;background:var(--teal);color:#fff;font-weight:700;font-size:21px;line-height:34px;text-align:center;border-radius:3px;letter-spacing:.5px}
  .ico{display:block;flex:none}
</style>
</head>
<body>
<main class="flyer">

  <svg class="abs hero-photo" viewBox="0 0 1100 500" role="img" aria-label="Photo of children running and playing football on a grassy park lawn">
    <defs>
      <linearGradient id="parkTones" x1="0" y1="0" x2="0" y2="1">
        <stop offset="0" stop-color="#4f7a3a"/>
        <stop offset=".5" stop-color="#8bb46b"/>
        <stop offset="1" stop-color="#5e8f3c"/>
      </linearGradient>
    </defs>
    <polygon points="572,0 1100,0 1100,492 619,247" fill="url(#parkTones)"/>
  </svg>

  <svg class="abs accent-stripe" viewBox="0 0 1100 300" aria-hidden="true">
    <polygon points="0,216 622,244 622,256 0,232" fill="var(--orange)"/>
  </svg>

  <div class="abs brand">
    <span class="brand-dot"></span>
    <span class="brand-name">Maple Grove Kids<br>Pediatrics</span>
  </div>

  <h1 class="abs welcome">
    <span class="l1">WELCOME TO</span>
    <span class="l2">MAPLE GROVE KIDS</span>
    <span class="l3">CARE PEDIATRIC!</span>
  </h1>
  <p class="abs welcome-sub">Where we believe it takes a community to raise a child. We are excited to be small yet important member of the community to help raise a healthy and happy child.</p>

  <div class="abs teddy" role="img" aria-label="Photo of a small child listening to a teddy bear with a toy stethoscope"></div>

  <div class="abs goal-band"></div>
  <div class="abs goal-pill">Our Goal is to provide</div>
  <p class="abs goal-text"><span class="purple">Personalized</span> and <span class="pink">Comprehensive care</span> collectively that consists of the Parent, Child, Provider Triangle.</p>
  <div class="abs note note-star" role="img" aria-label="Illustration of an orange sticky note with a pink star"></div>
  <div class="abs note note-rocket" role="img" aria-label="Illustration of a paper note with a rocket drawing"></div>
  <div class="abs note note-dream" role="img" aria-label="Illustration of a blue note reading Dream Big"></div>

  <div class="abs provider-photo" role="img" aria-label="Portrait photo of the pediatrician"></div>
  <div class="abs provider-tag">Meet Our Provider</div>

  <div class="abs bio">
    <p><span class="doc">Dr. Amira Haddon</span> is an experienced &amp; qualified Pediatrician, previously served the communities of Annandale and Alexandria, VA for several years.</p>
    <p>Where she was recognized in the Metro Living Top Doctors 2019 magazine as well as Top Female Doctor in the city of Annandale, Virginia. For past few years she had been serving the underserved population of Siler City, NC.</p>
    <p>She obtained her medical degree from the Crestmoor Medical College. After numerous research and observership positions in North Carolina including the Harlow Clinic, Northfield Medical Alliance and Eastern State University, and abroad including Riverside Children's Hospital and Eastgate Hospital, she decided to pursue her passion of working with children and trained in Pediatrics at Westbrook University of Health Sciences in El Paso, Texas.</p>
  </div>

  <p class="abs bio-wide">A devout mother of five, Dr Haddon recognizes the special care &amp; attention that children need and exercises her professional and maternal insight with her patients. She is multilingual in English, Hindi and Punjabi allowing patients from a variety of backgrounds to comfortably communicate with her. Her extensive travel has also allowed her to be sensitive to various cultures and is able to exercises her professional and maternal insight with her patients. She is multilingual in English, Hindi and Punjabi allowing patients from a variety of backgrounds to comfortably communicate with her. Her extensive travel has also allowed her to be sensitive to various cultures and is able to understand the needs of patients from different backgrounds. Caring for children is her passion. She believes that a visit to a Pediatrician should be warm and friendly and ensure an environment of comfort, diligence, discussion, and education. She also believes in building a relationship with the Patient/Parent by listening and creating a partnership to maintain and improve lifelong health.</p>

  <div class="abs footer-band"></div>
  <div class="abs kids-photo" role="img" aria-label="Photo of a smiling boy and girl in a cloud-shaped frame"></div>

  <p class="abs coming">COMING SOON <span class="teal">PEDIATRICIAN</span></p>
  <p class="abs accepting">Accepting new patients</p>
  <div class="abs red-band"><span>FREE 1ST CONSULTATION</span></div>
  <div class="abs blue-band"><span>We are planning on opening the clinic in December</span></div>

  <svg class="abs phone-icon" viewBox="0 0 40 40" aria-hidden="true">
    <rect width="40" height="40" rx="6" fill="var(--pink)"/>
    <path d="M13 10c1.5-1 3 0 4 2l1.5 3c.5 1 0 2-1 2.6l-1.2.8c1 2.6 3 4.6 5.6 5.6l.8-1.2c.6-1 1.6-1.5 2.6-1l3 1.5c2 1 3 2.5 2 4-1.5 2.5-4 3.5-7 2.2C17 27 13 23 11 17.5 9.8 14.5 10.8 11.8 13 10z" fill="#fff"/>
  </svg>
  <p class="abs phone-num">555-014-2287</p>
  <p class="abs web">
    <svg class="ico" width="12" height="12" viewBox="0 0 14 14" aria-hidden="true"><circle cx="7" cy="7" r="6" fill="none" stroke="var(--teal)" stroke-width="1.4"/><path d="M1 7h12M7 1c-3 3.5-3 8.5 0 12M7 1c3 3.5 3 8.5 0 12" fill="none" stroke="var(--teal)" stroke-width="1.2"/></svg>
    <span>www.maplegrovekids.example</span>
  </p>
  <p class="abs addr">
    <svg class="ico" width="12" height="16" viewBox="0 0 12 16" aria-hidden="true"><path d="M6 0C2.7 0 0 2.6 0 5.8 0 10 6 16 6 16s6-6 6-10.2C12 2.6 9.3 0 6 0zm0 8.2a2.4 2.4 0 110-4.8 2.4 2.4 0 010 4.8z" fill="var(--teal)"/></svg>
    <span>48 Linden Row, Suite 12, Fairbrook NC 27000</span>
  </p>
  <p class="abs contact2">
    <svg class="ico" width="15" height="13" viewBox="0 0 16 14" aria-hidden="true"><rect x="3" y="0" width="10" height="5" fill="var(--teal)"/><rect x="0" y="5" width="16" height="6" rx="1" fill="var(--teal)"/><rect x="3" y="9" width="10" height="5" fill="#fff" stroke="var(--teal)" stroke-width="1.2"/></svg>
    <span>555-014-9310</span>
    <span class="sep"></span>
    <svg class="ico" width="14" height="10" viewBox="0 0 15 11" aria-hidden="true"><rect x=".6" y=".6" width="13.8" height="9.8" fill="none" stroke="var(--teal)" stroke-width="1.2"/><path d="M.6.6l6.9 5.5L14.4.6" fill="none" stroke="var(--teal)" stroke-width="1.2"/></svg>
    <span>office@maplegrovekids.example</span>
  </p>
  <div class="abs register">REGISTER TODAY</div>

</main>
</body>
</html>
```